Buch-/E-Book-Cover für Tagebuchroman
sehr auf meine Wünsche eingegangen, schnell, hilfsbereit und sehr genau
Zielgruppe
Ich bin Schriftstellerin - mein Roman richtet sich an Jugendliche (12-16 Jahre), in erster Linie Mädchen.
Ich benötige ein Cover für e-book und Paperback.
Aufgabenstellung
Es sollte ein junges, flottes Cover sein. Das Buch ist ein Tagebuchroman, dh es könnte z.B. wie das Tagebuch der 14-jährigen Protagonistin gestaltet sein. (Buchtitel ist 'Kritzeleien aus Zimmer Neun')
zum Inhalt:
Die 14-jährige Lena ist – als Gedichte schreibende Pessimistin – eindeutig anders. Dabei möchte sie so gerne „dazugehören“! Zum Glück hat Lena einen genialen Plan: Sie beschließt, von nun an positiv zu denken. Doch da ist der neue Mathelehrer, bei dem sie immer so ein eigenartiges Bauchkribbeln bekommt, ein peinliches ClipWelle-Video taucht auf und die Erzfeindin in der Schule ist gemeiner denn je. Und dann zieht auch noch eine neue Familie ins Nachbarhaus: Deren Zwillinge – die coole Jule und der nervige Torben – stellen Lenas Leben komplett auf den Kopf…
Eine turbulente Geschichte über das Anderssein, Freundschaft und die erste Liebe…

```html
<!DOCTYPE html>
<html lang="de">
<head>
<meta charset="utf-8">
<title>Kritzeleien aus Zimmer Neun – Cover</title>
<link rel="stylesheet" href="https://fonts.googleapis.com/css2?family=Mr+Dafoe&family=Montserrat:wght@300&display=swap">
<style>
  :root {
    --backdrop: #e6e7e5;
    --cover-pink: #f4bcbc;
    --pattern-pink-light: #efb3b4;
    --pattern-pink-dark: #e3a5a7;
    --ink: #252222;
  }
  html, body {
    margin: 0;
    padding: 0;
    width: 1200px;
    height: 1200px;
    overflow: hidden;
    background: var(--backdrop);
  }
  .cover {
    position: absolute;
    left: 214px;
    top: 50px;
    width: 772px;
    height: 1100px;
    background: var(--cover-pink);
    overflow: hidden;
  }
  .balloon-pattern {
    position: absolute;
    left: 0;
    top: 0;
    width: 772px;
    height: 950px;
  }
  .title {
    position: absolute;
    inset: 0;
    margin: 0;
    color: var(--ink);
    font-weight: normal;
  }
  .title-script {
    position: absolute;
    font-family: "Mr Dafoe", cursive;
    line-height: 1;
    white-space: nowrap;
  }
  .title-top {
    left: 50px;
    top: 230px;
    font-size: 160px;
  }
  .title-middle {
    position: absolute;
    right: 90px;
    top: 500px;
    font-family: "Montserrat", sans-serif;
    font-weight: 300;
    font-size: 52px;
    letter-spacing: 2px;
    line-height: 1;
  }
  .title-bottom {
    left: 150px;
    top: 545px;
    font-size: 200px;
  }
</style>
</head>
<body>
  <main class="cover">
    <svg class="balloon-pattern" role="img" aria-label="Muster aus fein gezeichneten Heißluftballons, Luftschiffen und Wolken" viewBox="0 0 772 950" preserveAspectRatio="none">
      <defs>
        <linearGradient id="pattern-fade" x1="0" y1="0" x2="0" y2="1">
          <stop offset="0" stop-color="var(--pattern-pink-dark)"/>
          <stop offset="0.8" stop-color="var(--pattern-pink-light)"/>
          <stop offset="1" stop-color="var(--cover-pink)"/>
        </linearGradient>
      </defs>
      <rect width="772" height="950" fill="url(#pattern-fade)"/>
    </svg>
    <h1 class="title">
      <span class="title-script title-top">Kritzeleien</span>
      <span class="title-middle">AUS ZIMMER</span>
      <span class="title-script title-bottom">Neun</span>
    </h1>
  </main>
</body>
</html>
```